Healthy Meal Delivery Website needs a new face lift

Hi there,

The current website i have is super old and outdated.

I would like a beautiful modern site that has all the same content as the previous except with a a new, modern and trustworthy feel.

The current website is http://www.fennoxdinners.ca/

Target Market(s)

Diet Meal delivery, weight loss, healthy meal delivery

Industry/Entity Type

Food Service

Number of Pages Required

5+ page

Font styles to use
Sans Serif

Requirements
Must have
• Modern & Clean
Should not have
• Anything outdated or cheesy

```html
<!DOCTYPE html>
<html lang="en">
<head>
<meta charset="utf-8">
<title>Fennox Dinners – Fresh Customized Diet Meals</title>
<link href="https://fonts.googleapis.com/css2?family=Lato:wght@400;700;900&display=swap" rel="stylesheet">
<style>
:root{
  --blue:#29a9e0;
  --blue-dark:#1b8fc6;
  --ink:#1d1d1d;
  --text:#555;
  --muted:#777;
  --grey-bg:#f3f4f6;
  --line:#d9d9d9;
  --white:#fff;
}
*{margin:0;padding:0;box-sizing:border-box}
html,body{width:1200px;height:3622px;overflow:hidden}
body{font-family:'Lato',sans-serif;color:var(--text);background:var(--white);position:relative}
.abs{position:absolute}
.btn-solid{background:var(--blue);color:var(--white);border-radius:30px;font-weight:700;display:flex;align-items:center;justify-content:center;text-transform:uppercase;letter-spacing:.5px}
.btn-outline{border:2px solid var(--blue);color:var(--blue);border-radius:30px;font-weight:700;display:flex;align-items:center;justify-content:center;text-transform:uppercase;font-size:14px}

/* header */
.site-header{position:absolute;left:0;top:0;width:1200px;height:111px;background:var(--white)}
.brand{position:absolute;left:97px;top:24px;display:flex;align-items:center;gap:10px}
.brand-dot{width:22px;height:22px;border-radius:50%;background:var(--blue)}
.brand-name{font-size:30px;font-weight:900;color:var(--blue);line-height:1}
.top-contact{position:absolute;top:26px;left:528px;display:flex;gap:26px;font-size:15px;font-weight:700;color:var(--ink);align-items:center}
.top-contact span{display:flex;align-items:center;gap:8px}
.login{position:absolute;left:937px;top:14px;width:161px;height:49px;font-size:14px;gap:7px}
.main-nav{position:absolute;top:77px;left:367px;display:flex;gap:27px;font-size:14.5px;font-weight:700;color:var(--ink);text-transform:uppercase;align-items:center}
.main-nav .active{color:var(--blue)}

/* hero */
.hero{position:absolute;left:0;top:111px;width:1200px;height:529px;overflow:hidden;
  background:linear-gradient(100deg,#3a2416 0%,#5b3a24 35%,#6b4a30 50%,#8a8a7a 65%,#b9b7ab 100%)}
.hero-plate{position:absolute;left:525px;top:-120px;width:820px;height:820px;border-radius:50%;
  background:radial-gradient(circle at 45% 45%,#e08460 0%,#7aa04a 30%,#5c8c3a 55%,#e9e6df 72%,#d6d3cb 100%)}
.hero h1{position:absolute;left:96px;top:150px;width:620px;color:var(--white);font-size:42px;font-weight:900;line-height:58px}
.hero-cta{position:absolute;left:99px;top:365px;width:171px;height:50px;border:2px solid var(--white);border-radius:30px;color:var(--white);font-weight:700;font-size:15px;display:flex;align-items:center;justify-content:center}
.hero-dots{position:absolute;left:552px;top:464px;display:flex;gap:6px}
.hero-dots i{width:22px;height:5px;background:rgba(255,255,255,.75);display:block}
.hero-dots i:first-child{background:var(--blue)}

/* welcome */
.welcome{position:absolute;left:0;top:640px;width:1200px;height:620px}
.section-title{font-size:36px;font-weight:900;color:var(--ink);text-align:center;text-transform:uppercase}
.welcome .section-title{position:absolute;top:80px;width:100%}
.welcome-sub{position:absolute;top:137px;width:100%;text-align:center;color:var(--blue);font-weight:700;font-size:16px}
.welcome-text{position:absolute;top:183px;left:240px;width:720px;text-align:center;font-size:13px;line-height:25px;color:var(--muted)}
.feature{position:absolute;width:330px;display:flex;gap:22px}
.feature-icon{width:97px;height:97px;border-radius:50%;border:1.5px solid #cfcfcf;display:flex;align-items:center;justify-content:center;flex-shrink:0}
.feature h3{font-size:17px;font-weight:700;color:var(--ink);text-transform:uppercase;margin-top:16px;margin-bottom:12px}
.feature p{font-size:13.5px;line-height:23px;color:#444;width:175px}

/* programs */
.programs{position:absolute;left:0;top:1260px;width:1200px;height:785px;background:var(--grey-bg)}
.programs .section-title{position:absolute;top:62px;width:100%}
.programs-sub{position:absolute;top:120px;width:100%;text-align:center;font-size:18px;font-weight:700;color:var(--ink)}
.programs .view-menu{position:absolute;left:526px;top:164px;width:148px;height:53px;font-size:15px}
.program{position:absolute;top:268px;width:316px}
.program-photo{width:316px;height:210px}
.program h3{font-size:22px;font-weight:700;color:var(--ink);margin-top:34px}
.program p{font-size:13.5px;line-height:24px;color:var(--muted);margin-top:14px;height:72px}
.program .btn-outline{width:128px;height:46px;margin-top:32px}

/* how it works */
.how{position:absolute;left:0;top:2045px;width:1200px;height:690px}
.how .section-title{position:absolute;top:76px;width:100%}
.step{position:absolute;top:176px;width:260px;text-align:center}
.step-circle{width:159px;height:159px;border-radius:50%;border:1.5px solid #c9c9c9;margin:0 auto;display:flex;align-items:center;justify-content:center}
.step-art{width:74px;height:74px;border-radius:18px}
.step h3{font-size:17.5px;font-weight:700;color:var(--ink);margin-top:30px}
.step p{font-size:13.5px;line-height:25px;color:#555;margin-top:16px;padding:0 25px}
.how .get-started{position:absolute;left:500px;top:533px;width:200px;height:58px;font-size:15px}

/* reviews */
.reviews{position:absolute;left:0;top:2735px;width:1200px;height:464px;overflow:hidden;
  background:linear-gradient(135deg,#2aa5dd 0%,#3cb4e6 45%,#2a9fd8 100%)}
.reviews-glow{position:absolute;left:330px;top:90px;width:560px;height:330px;border-radius:50%;background:radial-gradient(ellipse,rgba(255,255,255,.28),rgba(255,255,255,0) 70%)}
.reviews .section-title{position:absolute;top:64px;width:100%;color:var(--white)}
.review{position:absolute;top:191px;width:307px;height:195px;border:2px solid rgba(255,255,255,.85);text-align:center;color:var(--white)}
.avatar{position:absolute;left:111px;top:-42px;width:85px;height:85px;border-radius:50%;border:3px solid var(--white);background:linear-gradient(#d9b8a0,#a57c62)}
.review p{font-style:italic;font-size:12.5px;line-height:21px;padding:72px 24px 0}
.review h4{font-size:17px;font-weight:700;margin-top:10px}
.arrow{position:absolute;top:3000px;width:38px;height:38px;border-radius:50%;background:rgba(255,255,255,.85);display:flex;align-items:center;justify-content:center}

/* footer */
.site-footer{position:absolute;left:0;top:3199px;width:1200px;height:423px;background:var(--white)}
.footer-brand{position:absolute;left:97px;top:168px;display:flex;align-items:center;gap:12px}
.footer-brand .brand-name{font-size:34px}
.footer-col{position:absolute;top:100px}
.footer-col h4{font-size:19px;font-weight:700;color:var(--ink);margin-bottom:20px}
.footer-links li{list-style:none;font-size:12.5px;color:#555;line-height:23px}
.newsletter p{font-size:12.5px;line-height:22px;color:#444;width:260px}
.email-field{width:250px;border-bottom:1px solid var(--line);font-size:12px;color:#999;padding:14px 0 6px;margin-top:8px}
.subscribe{width:105px;height:36px;font-size:11px;margin-top:16px}
.contact-item{display:flex;gap:16px;font-size:12.5px;line-height:19px;color:#444;margin-bottom:18px}
.contact-item svg{flex-shrink:0;margin-top:2px}
.footer-rule{position:absolute;left:97px;top:340px;width:1006px;height:1px;background:var(--line)}
.copyright{position:absolute;left:97px;top:368px;font-size:11.5px;color:#555}
.social{position:absolute;left:978px;top:363px;display:flex;gap:8px}
.social i{width:25px;height:25px;border-radius:50%;border:1.5px solid var(--blue);display:block}
</style>
</head>
<body>

<header class="site-header">
  <div class="brand"><span class="brand-dot"></span><span class="brand-name">Fennox Dinners</span></div>
  <div class="top-contact">
    <span><svg width="15" height="15" viewBox="0 0 24 24" fill="#29a9e0"><path d="M6.6 10.8a15.1 15.1 0 0 0 6.6 6.6l2.2-2.2c.3-.3.7-.4 1-.2 1.1.4 2.3.6 3.6.6.6 0 1 .4 1 1V20c0 .6-.4 1-1 1A17 17 0 0 1 3 4c0-.6.4-1 1-1h3.5c.6 0 1 .4 1 1 0 1.3.2 2.5.6 3.6.1.3 0 .7-.2 1z"/></svg>416-555-0142</span>
    <span style="color:#ccc">|</span>
    <span><svg width="15" height="13" viewBox="0 0 24 20" fill="#29a9e0"><path d="M2 0h20a2 2 0 0 1 2 2v16a2 2 0 0 1-2 2H2a2 2 0 0 1-2-2V2a2 2 0 0 1 2-2zm10 9L2 3v2l10 6 10-6V3z"/></svg>hello@fennoxdinners.ca</span>
  </div>
  <div class="login btn-solid"><svg width="12" height="12" viewBox="0 0 24 24" fill="#fff"><circle cx="12" cy="7" r="5"/><path d="M2 24c0-6 4.5-10 10-10s10 4 10 10z"/></svg>Customer Login</div>
  <nav class="main-nav">
    <span class="active">Home</span><span>How it works</span><span>Pricing</span><span>Sample Menu</span><span>Celebrity</span><span>F.A.Q.</span><span>Contact</span>
    <svg width="14" height="14" viewBox="0 0 24 24" fill="none" stroke="#1d1d1d" stroke-width="3"><circle cx="10" cy="10" r="7"/><path d="M15 15l7 7"/></svg>
  </nav>
</header>

<section class="hero">
  <div class="hero-plate" role="img" aria-label="Plate of grilled salmon with asparagus and cherry tomatoes on a wooden table"></div>
  <h1>Fresh Customized Diet Meals Delivered Daily Toronto and Canada Wide</h1>
  <div class="hero-cta">ORDER NOW!</div>
  <div class="hero-dots"><i></i><i></i><i></i><i></i></div>
</section>

<section class="welcome">
  <h2 class="section-title">Welcome to Fennox Dinners</h2>
  <p class="welcome-sub">Fresh diet gourmet meals delivered by Fennox</p>
  <p class="welcome-text">Fresh diet meal delivery Toronto and Canada wide is our signature fresh gourmet diet meal delivery program designed for healthy living &amp; weight loss management. Diet meal delivery Toronto has a creative gourmet menu that uses exotic flavors and ingredients to enhance your dining experience</p>

  <div class="feature" style="left:99px;top:355px">
    <div class="feature-icon"><svg width="40" height="40" viewBox="0 0 24 24" fill="#29a9e0"><path d="M2 10h4v12H2zM8 21V10l5-8c1.5 0 2.5 1 2.3 2.5L14.5 9H21c1.2 0 2 1 1.8 2.2l-1.6 8.3c-.2 1-1 1.5-2 1.5z"/></svg></div>
    <div><h3>Benefits</h3><p>Fresh diet meal delivery daily</p></div>
  </div>
  <div class="feature" style="left:454px;top:355px">
    <div class="feature-icon"><svg width="36" height="40" viewBox="0 0 20 24" fill="none" stroke="#29a9e0" stroke-width="1.6"><path d="M2 1h11l5 5v17H2z"/><path d="M13 1v5h5M5 11h10M5 15h10M5 19h10"/></svg></div>
    <div><h3>Menu</h3><p>Inspired fresh gourmet Fennox meals</p></div>
  </div>
  <div class="feature" style="left:816px;top:355px">
    <div class="feature-icon"><svg width="40" height="34" viewBox="0 0 24 20" fill="#29a9e0"><rect x="0" y="0" width="7" height="5.5" rx="1"/><rect x="8.5" y="0" width="7" height="5.5" rx="1"/><rect x="17" y="0" width="7" height="5.5" rx="1"/><rect x="0" y="7.2" width="7" height="5.5" rx="1"/><rect x="8.5" y="7.2" width="7" height="5.5" rx="1"/><rect x="17" y="7.2" width="7" height="5.5" rx="1"/><rect x="0" y="14.4" width="7" height="5.5" rx="1"/><rect x="8.5" y="14.4" width="7" height="5.5" rx="1"/><rect x="17" y="14.4" width="7" height="5.5" rx="1"/></svg></div>
    <div><h3>Variety</h3><p>60 Day Menu Rotation</p></div>
  </div>
  <div class="feature" style="left:99px;top:485px">
    <div class="feature-icon"><svg width="42" height="34" viewBox="0 0 30 24" fill="#29a9e0"><circle cx="15" cy="6" r="5"/><circle cx="5" cy="8" r="3.5"/><circle cx="25" cy="8" r="3.5"/><path d="M7 24c0-6 3.5-11 8-11s8 5 8 11zM0 22c0-5 2-8 5-8 1.5 0 2.5.5 3.3 1.5C6.5 17.5 6 20 6 22zM30 22c0-5-2-8-5-8-1.5 0-2.5.5-3.3 1.5 1.8 2 2.3 4.5 2.3 6.5z"/></svg></div>
    <div><h3>Customization</h3><p>Every fresh Fennox meal is personally customized</p></div>
  </div>
  <div class="feature" style="left:454px;top:485px">
    <div class="feature-icon"><svg width="44" height="30" viewBox="0 0 32 22" fill="#29a9e0"><path d="M0 2h19v14H0zM20 6h6l5 6v4h-11z"/><circle cx="6" cy="18" r="3.5"/><circle cx="25" cy="18" r="3.5"/></svg></div>
    <div><h3>Delivery</h3><p>Fresh diet meal delivery daily Toronto and Canada wide</p></div>
  </div>
  <div class="feature" style="left:816px;top:485px">
    <div class="feature-icon"><svg width="40" height="40" viewBox="0 0 24 24" fill="none" stroke="#29a9e0" stroke-width="2.4"><path d="M3 15v-3a9 9 0 0 1 18 0v3"/><rect x="2" y="14" width="5" height="7" rx="1.5" fill="#29a9e0"/><rect x="17" y="14" width="5" height="7" rx="1.5" fill="#29a9e0"/></svg></div>
    <div><h3>Customer Service</h3><p>Personal Nutritionist available 7 days a week</p></div>
  </div>
</section>

<section class="programs">
  <h2 class="section-title">Our Meal Programs</h2>
  <p class="programs-sub">See What's on the Menu!</p>
  <div class="view-menu btn-solid">View Menu</div>

  <article class="program" style="left:99px">
    <div class="program-photo" role="img" aria-label="Roasted glazed chicken on a dark plate" style="background:radial-gradient(circle at 50% 55%,#c9541e 0%,#8a2e12 45%,#2a1a14 100%)"></div>
    <h3>Enjoy Our Gourmet Menu</h3>
    <p>Every fresh diet meal delivered is prepared with the finest ingredients available and has a creative menu that uses unique</p>
    <div class="btn-outline">Order Now!</div>
  </article>
  <article class="program" style="left:442px">
    <div class="program-photo" role="img" aria-label="Hand holding a phone over a table of fresh salads" style="background:linear-gradient(135deg,#e7dccb 0%,#b5c98a 40%,#d0a06a 70%,#efe6d8 100%)"></div>
    <h3>Customized For You</h3>
    <p>The diet meal delivery program offers the widest selection of healthy options regarding your ingredients preference, allergies..</p>
    <div class="btn-outline">Order Now!</div>
  </article>
  <article class="program" style="left:785px">
    <div class="program-photo" role="img" aria-label="Sliced grilled steak over green salad" style="background:radial-gradient(circle at 50% 55%,#7a4a32 0%,#5c8a3a 45%,#dcdad2 85%)"></div>
    <h3>Pause Your Program Anytime</h3>
    <p>You are welcome to pause and restart your meal program at anytime. Our customers lead busy lives, therefore if you need to post-pone..</p>
    <div class="btn-outline">Order Now!</div>
  </article>
</section>

<section class="how">
  <h2 class="section-title">How It Works</h2>
  <div class="step" style="left:80px">
    <div class="step-circle"><div class="step-art" role="img" aria-label="Illustration of a folded menu" style="background:#e39a3b"></div></div>
    <h3>Choose your meal plan</h3>
    <p>Once these levels are reached and maintained, the body enters a state of hormonal balance</p>
  </div>
  <div class="step" style="left:341px">
    <div class="step-circle"><div class="step-art" role="img" aria-label="Illustration of a bowl with vegetables and utensils" style="background:linear-gradient(#f0c040,#3a86c8)"></div></div>
    <h3>Customize your meals</h3>
    <p>Once these levels are reached and maintained, the body enters a state of hormonal balance</p>
  </div>
  <div class="step" style="left:599px">
    <div class="step-circle"><div class="step-art" role="img" aria-label="Illustration of a map with a delivery route" style="border-radius:50%;background:radial-gradient(#f0d060,#e0783a 55%,#6aa84f)"></div></div>
    <h3>Delivered to you</h3>
    <p>Once these levels are reached and maintained, the body enters a state of hormonal balance</p>
  </div>
  <div class="step" style="left:857px">
    <div class="step-circle"><div class="step-art" role="img" aria-label="Illustration of a microwave oven" style="height:54px;background:#e0506a"></div></div>
    <h3>Heat &amp; eat</h3>
    <p>Once these levels are reached and maintained, the body enters a state of hormonal balance</p>
  </div>
  <div class="get-started btn-solid">Get Started Now!</div>
</section>

<section class="reviews">
  <div class="reviews-glow" role="img" aria-label="Soft blurred photo of a plated salad under a blue tint"></div>
  <h2 class="section-title">Customer Reviews</h2>
  <div class="review" style="left:99px">
    <div class="avatar" role="img" aria-label="Customer portrait"></div>
    <p>Nam libero tempore, cum soluta nobis est eligendi optio cumque nihil impedit quo minus id quod maxime placea</p>
    <h4>Nora Ellison</h4>
  </div>
  <div class="review" style="left:447px">
    <div class="avatar" role="img" aria-label="Customer portrait"></div>
    <p>Nam libero tempore, cum soluta nobis est eligendi optio cumque nihil impedit quo minus id quod maxime placea</p>
    <h4>Tess Whitford</h4>
  </div>
  <div class="review" style="left:795px">
    <div class="avatar" role="img" aria-label="Customer portrait"></div>
    <p>Nam libero tempore, cum soluta nobis est eligendi optio cumque nihil impedit quo minus id quod maxime placea</p>
    <h4>Dane Carrow</h4>
  </div>
</section>
<div class="arrow" style="left:27px"><svg width="12" height="14" viewBox="0 0 12 14"><path d="M9 1L3 7l6 6" fill="none" stroke="#29a9e0" stroke-width="2.5"/></svg></div>
<div class="arrow" style="left:1133px"><svg width="12" height="14" viewBox="0 0 12 14"><path d="M3 1l6 6-6 6" fill="none" stroke="#29a9e0" stroke-width="2.5"/></svg></div>

<footer class="site-footer">
  <div class="footer-brand"><span class="brand-dot"></span><span class="brand-name">Fennox Dinners</span></div>

  <div class="footer-col" style="left:391px">
    <h4>Information</h4>
    <ul class="footer-links">
      <li>Home</li><li>How It Works</li><li>Pricing</li><li>Sample Menu</li><li>Celebrity</li><li>F.A.Q.</li><li>Contact</li>
    </ul>
  </div>

  <div class="footer-col newsletter" style="left:575px">
    <h4>Newsletter Subscription</h4>
    <p>Register your Email Address to get information about us</p>
    <div class="email-field">Email Address</div>
    <div class="subscribe btn-solid">Subscribe</div>
  </div>

  <div class="footer-col" style="left:891px">
    <h4>Contact Us</h4>
    <div class="contact-item"><svg width="11" height="15" viewBox="0 0 12 16" fill="#29a9e0"><path d="M6 0a6 6 0 0 1 6 6c0 4.5-6 10-6 10S0 10.5 0 6a6 6 0 0 1 6-6zm0 3.5a2.5 2.5 0 1 0 0 5 2.5 2.5 0 0 0 0-5z"/></svg><span>118 Marlow Crescent<br>Toronto, ON M4T 2B6</span></div>
    <div class="contact-item"><svg width="11" height="15" viewBox="0 0 12 16" fill="#29a9e0"><path d="M6 0a6 6 0 0 1 6 6c0 4.5-6 10-6 10S0 10.5 0 6a6 6 0 0 1 6-6zm0 3.5a2.5 2.5 0 1 0 0 5 2.5 2.5 0 0 0 0-5z"/></svg><span>4410 Ridgefield Avenue, Suite 210<br>Columbus, Ohio 43215</span></div>
    <div class="contact-item"><svg width="12" height="12" viewBox="0 0 24 24" fill="#29a9e0"><path d="M6.6 10.8a15.1 15.1 0 0 0 6.6 6.6l2.2-2.2c.3-.3.7-.4 1-.2 1.1.4 2.3.6 3.6.6.6 0 1 .4 1 1V20c0 .6-.4 1-1 1A17 17 0 0 1 3 4c0-.6.4-1 1-1h3.5c.6 0 1 .4 1 1 0 1.3.2 2.5.6 3.6.1.3 0 .7-.2 1z"/></svg><span>416-555-0142</span></div>
    <div class="contact-item"><svg width="12" height="10" viewBox="0 0 24 20" fill="#29a9e0"><path d="M2 0h20a2 2 0 0 1 2 2v16a2 2 0 0 1-2 2H2a2 2 0 0 1-2-2V2a2 2 0 0 1 2-2zm10 9L2 3v2l10 6 10-6V3z"/></svg><span>hello@fennoxdinners.ca</span></div>
  </div>

  <div class="footer-rule"></div>
  <p class="copyright">Copyrights © 2018, Fennox Dinners. All rights reserved.</p>
  <div class="social"><i></i><i></i><i></i><i></i></div>
</footer>

</body>
</html>
```